Rock band business card design

I need an edgy double sided business card to hand out at music events and to send out to radio.

It needs to display our logo, web address and social media icons (linkora, plumbit, vostramesh).

Colour scheme to match our website (www.thedrelliq.com)

Please include this quote:
The clock is turning... a reckoning... THE DRELLIQ.

Logo files have been attached.

I look forward to seeing your designs!

Target Market(s)

radio stations, music fans.

Industry/Entity Type

Events

Requirements
Must have
• Website address, social media icons, quote, colour scheme to match www.thedrelliq.com

```html
<!DOCTYPE html>
<html lang="en">
<head>
<meta charset="utf-8">
<title>The Drelliq – Business Card</title>
<link rel="stylesheet" href="https://fonts.googleapis.com/css2?family=Open+Sans:wght@300;400;700&display=swap">
<style>
  :root {
    --paper: #ffffff;
    --card-base: #f7f0b8;
    --card-pale: #fbf6d2;
    --sun-core: #fff6a8;
    --sun-mid: #f6d83c;
    --sun-edge: #e9b92a;
    --quote-brown: #7a5a3a;
    --logo-brown: #5a3418;
    --emblem-tone: #b89a6e;
    --ink: #1e1a14;
    --crop: #222222;
    --plumbit: #2c8fd6;
    --linkora: #2f54a3;
    --vostramesh: #d9322a;
    --korvid: #8c8c8c;
  }
  * { margin: 0; padding: 0; box-sizing: border-box; }
  html, body { width: 1200px; height: 725px; overflow: hidden; background: var(--paper); }
  body { position: relative; font-family: "Open Sans", sans-serif; }

  .crop-marks { position: absolute; inset: 0; }

  .card {
    position: absolute; left: 36px; top: 36px; width: 1128px; height: 650px;
    background: linear-gradient(180deg, var(--card-pale) 0%, var(--card-base) 100%);
    overflow: hidden;
  }
  .sunrise-band {
    position: absolute; left: 0; top: 0; width: 100%; height: 242px;
    background:
      radial-gradient(ellipse 420px 220px at 590px 140px, var(--sun-core) 0%, rgba(255,246,168,0) 75%),
      linear-gradient(180deg, var(--sun-mid) 0%, var(--sun-edge) 55%, var(--sun-mid) 85%, rgba(246,216,60,0.2) 100%);
  }
  .tagline {
    position: absolute; left: 106px; top: 36px;
    font-weight: 700; font-size: 32px; color: var(--quote-brown); white-space: nowrap;
  }
  .holder-name {
    position: absolute; left: 98px; top: 198px;
    font-weight: 300; font-size: 48px; color: var(--ink); letter-spacing: -0.5px;
  }
  .band-name {
    position: absolute; left: 770px; top: 254px; width: 300px; text-align: center;
    font-weight: 400; font-size: 44px; color: var(--logo-brown); white-space: nowrap;
  }
  .band-emblem {
    position: absolute; left: 786px; top: 318px; width: 264px; height: 246px;
    border-radius: 6px;
    background: radial-gradient(ellipse at 50% 40%, rgba(184,154,110,0.55) 0%, rgba(184,154,110,0.2) 100%);
  }
  .band-url {
    position: absolute; left: 700px; top: 562px; width: 400px; text-align: center;
    font-size: 32px; color: var(--ink); white-space: nowrap;
  }
  .social-row {
    position: absolute; left: 96px; top: 532px; display: flex; align-items: center; gap: 22px;
  }
  .social-item { display: flex; align-items: center; gap: 8px; font-weight: 700; font-size: 22px; color: var(--logo-brown); }
  .social-square { width: 30px; height: 30px; border-radius: 5px; }
  .social-square.plumbit { background: var(--plumbit); }
  .social-square.linkora { background: var(--linkora); }
  .social-square.vostramesh { background: var(--vostramesh); }
  .social-square.korvid { background: var(--korvid); }
</style>
</head>
<body>
  <svg class="crop-marks" width="1200" height="725" viewBox="0 0 1200 725" aria-hidden="true">
    <g stroke="var(--crop)" stroke-width="1">
      <line x1="36" y1="0" x2="36" y2="24"/><line x1="0" y1="36" x2="24" y2="36"/>
      <line x1="1164" y1="0" x2="1164" y2="24"/><line x1="1176" y1="36" x2="1200" y2="36"/>
      <line x1="36" y1="701" x2="36" y2="725"/><line x1="0" y1="686" x2="24" y2="686"/>
      <line x1="1164" y1="701" x2="1164" y2="725"/><line x1="1176" y1="686" x2="1200" y2="686"/>
    </g>
  </svg>

  <section class="card">
    <div class="sunrise-band" role="img" aria-label="Background artwork: golden sunrise glow"></div>
    <p class="tagline">The clock is turning... a reckoning... THE DRELLIQ.</p>
    <h1 class="holder-name">Cal Morrow</h1>

    <p class="band-name">THE DRELLIQ</p>
    <div class="band-emblem" role="img" aria-label="Band emblem artwork"></div>

    <p class="band-url">www.thedrelliq.com</p>

    <div class="social-row">
      <span class="social-item"><span class="social-square plumbit"></span>plumbit</span>
      <span class="social-item"><span class="social-square linkora"></span>linkora</span>
      <span class="social-item"><span class="social-square vostramesh"></span>vostramesh</span>
      <span class="social-item"><span class="social-square korvid"></span>Korvid Sound</span>
    </div>
  </section>
</body>
</html>
```